Boutique Fitness Facility needs a new meal plan design that is as hot as our workouts!

We are about to host our 6 week Heatwave Reset program and we need to have a great looking meal plan handout created that we can give to all of our participants.

I have attached an example of our current full meal plan, for a reference only.

As in the example I've provided, I'd like to have certain areas color coded such as the proteins being Blue, Fats -yellow, Carbs - orange and veggies- green.

These colors will corollate to the Breakfast - snack - lunch - snack - Dinner graph that I've provided and would like to have added to the new handout.

I would like our logo placed at the top and beneath the logo have the text "Heatwave Reset Challenge"

The flyer should be of a summer influence in colors and design and
All text should be easy to read.

Thank you and I look forward to seeing your design!

```html
<!DOCTYPE html>
<html lang="en">
<head>
<meta charset="utf-8">
<title>FitForge – Heatwave Reset Challenge Meal Plan</title>
<link href="https://fonts.googleapis.com/css2?family=Barlow+Condensed:ital,wght@0,600;0,700;0,800;1,800&family=Barlow+Semi+Condensed:wght@500;600;700&family=Titan+One&family=Amatic+SC:wght@700&display=swap" rel="stylesheet">
<style>
  :root{
    --stage:#000000;
    --violet:#5a2fd4;
    --sky-blue:#1f84e6;
    --sky-pale:#d6ecfb;
    --fat-yellow:#f7c81e;
    --protein-blue:#1e88e5;
    --carb-orange:#f6911e;
    --veg-green:#22a84a;
    --title-yellow:#ffd21f;
    --title-orange:#ff8a00;
    --band-black:#0b0b0b;
    --peach-top:#f9c393;
    --peach-bottom:#ffe3c6;
    --ink-brown:#6a3412;
    --link-blue:#1d6fe0;
    --hub-grey:#b9b9b9;
    --white:#ffffff;
  }
  *{margin:0;padding:0;box-sizing:border-box;}
  html,body{width:1200px;height:1200px;overflow:hidden;background:var(--stage);}
  body{position:relative;font-family:"Barlow Semi Condensed",Arial,sans-serif;}

  .handout{position:absolute;left:220px;top:92px;width:796px;height:1029px;overflow:hidden;
    background:linear-gradient(180deg,var(--white) 0%,var(--white) 22%,var(--sky-pale) 60%,var(--sky-pale) 100%);}

  .header-band{position:absolute;left:0;top:0;width:796px;height:260px;}

  .brand-name{position:absolute;left:30px;top:26px;font-family:"Barlow Condensed",sans-serif;
    font-weight:800;font-size:70px;line-height:1;color:var(--title-yellow);letter-spacing:1px;}

  .title{position:absolute;left:360px;top:22px;width:430px;text-align:center;}
  .title-main{display:block;font-family:"Titan One",sans-serif;font-size:66px;line-height:1;
    background:linear-gradient(180deg,var(--title-yellow) 20%,var(--title-orange) 95%);
    -webkit-background-clip:text;background-clip:text;color:transparent;
    -webkit-text-stroke:2px var(--white);}
  .title-sub{display:block;margin-top:4px;font-family:"Amatic SC",cursive;font-weight:700;font-size:78px;
    line-height:1;color:var(--white);letter-spacing:6px;
    text-shadow:2px 2px 0 #2a3a8a,-1px -1px 0 #2a3a8a,1px -1px 0 #2a3a8a,-1px 1px 0 #2a3a8a;}

  .sun{position:absolute;left:598px;top:196px;width:180px;height:180px;border-radius:50%;
    background:radial-gradient(circle,#fff15a 0%,#ffd21f 55%,#ffb300 100%);z-index:3;}
  .challenge-tag{position:absolute;left:598px;top:263px;width:180px;text-align:center;z-index:4;
    font-family:"Barlow Condensed",sans-serif;font-style:italic;font-weight:800;font-size:36px;
    color:#4626b5;transform:rotate(-8deg);}

  .palm-leaf{position:absolute;left:-20px;top:240px;width:230px;height:110px;border-radius:50%;
    background:linear-gradient(120deg,#2f8f2f,#8cc63f);transform:rotate(18deg);opacity:.85;z-index:2;}

  .food-dome{position:absolute;left:4px;top:215px;width:788px;height:500px;display:flex;overflow:hidden;
    border-radius:394px 394px 0 0 / 330px 330px 0 0;}
  .food-group{position:relative;color:var(--white);}
  .food-group.fats{width:226px;background:var(--fat-yellow);}
  .food-group.protein{width:173px;background:var(--protein-blue);}
  .food-group.carbs{width:168px;background:var(--carb-orange);}
  .food-group.veggies{width:221px;background:var(--veg-green);}

  .group-title{position:absolute;font-family:"Barlow Condensed",sans-serif;font-style:italic;font-weight:800;
    font-size:38px;line-height:1;color:var(--white);letter-spacing:.5px;}
  .fats .group-title{color:var(--carb-orange);left:70px;top:240px;}
  .protein .group-title{left:22px;top:62px;}
  .carbs .group-title{left:14px;top:62px;}
  .veggies .group-title{left:12px;top:240px;}

  .icon-set{position:absolute;border-radius:14px;background:rgba(255,255,255,.32);}
  .fats .icon-set{left:80px;top:100px;width:120px;height:120px;}
  .protein .icon-set{left:20px;top:108px;width:134px;height:70px;}
  .carbs .icon-set{left:20px;top:108px;width:128px;height:70px;}
  .veggies .icon-set{left:14px;top:118px;width:110px;height:105px;}

  .food-list{position:absolute;list-style:none;font-weight:600;font-size:14px;line-height:17.6px;}
  .fats .food-list{left:52px;top:290px;}
  .protein .food-list{left:14px;top:190px;}
  .carbs .food-list{left:14px;top:190px;}
  .veggies .food-list{left:12px;top:288px;}
  .food-list .indent{padding-left:34px;}

  .meal-band{position:absolute;left:0;top:672px;width:796px;height:140px;}

  .meal-wheel{position:absolute;width:96px;height:96px;}
  .wheel-breakfast{left:44px;top:700px;}
  .wheel-lunch{left:354px;top:700px;}
  .wheel-dinner{left:662px;top:700px;}

  .flow-arrow{position:absolute;width:56px;height:36px;}
  .snack{position:absolute;width:110px;text-align:center;}
  .snack-pill{display:block;height:24px;border-radius:12px;background:var(--veg-green);color:var(--white);
    font-family:"Barlow Condensed",sans-serif;font-weight:700;font-size:18px;line-height:24px;letter-spacing:1px;}
  .snack-note{display:block;margin-top:6px;color:var(--white);font-size:11px;font-weight:600;white-space:nowrap;}
  .snack-one{left:186px;top:730px;}
  .snack-two{left:498px;top:730px;}

  .tips{position:absolute;left:0;top:790px;width:796px;height:239px;}
  .tips-bg{position:absolute;inset:0;}
  .frond-deco{position:absolute;right:40px;top:60px;width:200px;height:150px;border-radius:50%;
    background:rgba(255,255,255,.22);}
  .frond-deco.left{left:250px;right:auto;top:130px;width:160px;height:110px;}

  .tips-title{position:absolute;left:0;top:14px;width:796px;text-align:center;
    font-family:"Barlow Condensed",sans-serif;font-style:italic;font-weight:800;font-size:34px;line-height:1;}
  .tips-title .lead{color:var(--link-blue);}
  .tips-title .accent{color:var(--title-orange);}

  .tips-body{position:absolute;left:34px;top:56px;width:730px;color:var(--ink-brown);font-size:13px;
    line-height:15.6px;font-weight:500;}
  .tips-intro{font-weight:700;text-transform:uppercase;margin-bottom:1px;}
  .tip-list{list-style:none;}
  .tip-name{color:var(--link-blue);font-weight:700;text-decoration:underline;}
  .tip-list li .body{color:#4a2a12;}
  .credit{position:absolute;right:14px;bottom:6px;font-size:9px;color:#3b3b3b;font-style:italic;}
</style>
</head>
<body>
<main class="handout">

  <svg class="header-band" viewBox="0 0 796 260" aria-hidden="true">
    <defs>
      <linearGradient id="headerGrad" x1="0" y1="0" x2="1" y2="0">
        <stop offset="0" stop-color="#5a2fd4"/>
        <stop offset="1" stop-color="#1f84e6"/>
      </linearGradient>
    </defs>
    <path d="M0 0 H796 V150 Q600 245 400 200 Q200 160 0 225 Z" fill="url(#headerGrad)"/>
  </svg>

  <div class="brand-name">FitForge</div>

  <h1 class="title">
    <span class="title-main">HEATWAVE</span>
    <span class="title-sub">RESET</span>
  </h1>

  <div class="palm-leaf" role="img" aria-label="Palm frond illustration"></div>

  <div class="sun" role="img" aria-label="Bright summer sun burst"></div>
  <div class="challenge-tag">CHALLENGE!</div>

  <section class="food-dome">
    <div class="food-group fats">
      <div class="icon-set" role="img" aria-label="Icons of avocado, olive oil and nuts"></div>
      <h2 class="group-title">FATS</h2>
      <ul class="food-list">
        <li>¼ - ½ Avocado</li>
        <li>1 tbs Olive Oil</li>
        <li>1 small handful Almonds,</li>
        <li class="indent">Walnuts, Cashews</li>
      </ul>
    </div>
    <div class="food-group protein">
      <h2 class="group-title">PROTEIN</h2>
      <div class="icon-set" role="img" aria-label="Icons of eggs, steak, fish and cheese"></div>
      <ul class="food-list">
        <li>4-6 oz Chicken Breast</li>
        <li>4-6oz Turkey Breast</li>
        <li>4-6 oz Filet Mignon</li>
        <li>4-6 oz Flank Steak</li>
        <li>4-6 oz Salmon</li>
        <li>4-6 oz Tuna</li>
        <li>4-6 oz Cod</li>
        <li>4-6 oz Cottage Cheese</li>
        <li>4-6 oz Greek Yogurt</li>
        <li>4-6 oz Tofu</li>
        <li>3 -5 egg whites</li>
        <li class="indent">+ 1 whole egg</li>
      </ul>
    </div>
    <div class="food-group carbs">
      <h2 class="group-title">CARBS</h2>
      <div class="icon-set" role="img" aria-label="Icons of apple, rice bowl, sweet potato and berries"></div>
      <ul class="food-list">
        <li>3 – 4oz Sweet Potato</li>
        <li>¼ - ½ cup White Rice</li>
        <li>¼ - ½ cup Quinoa</li>
        <li>¼ - ½ cup Oatmeal</li>
        <li>¾ cup Blueberries</li>
        <li>¾ cup Strawberries</li>
        <li>¾ cup Raspberries</li>
        <li>1 med. Apple</li>
        <li>1 small orange</li>
        <li>1 small grapefruit</li>
      </ul>
    </div>
    <div class="food-group veggies">
      <div class="icon-set" role="img" aria-label="Icons of carrot, broccoli, pepper and zucchini"></div>
      <h2 class="group-title">VEGGIES</h2>
      <ul class="food-list">
        <li>1 Scoop Powdered Greens</li>
        <li>1 Cup Sautéed Spinach</li>
        <li>1 Cup Sautéed Kale, Broccoli</li>
        <li>1 Cup Sautéed Bell Pepper</li>
        <li>1 Cup Sautéed Carrots</li>
        <li>1 Cup Sautéed Zucchini</li>
      </ul>
    </div>
  </section>

  <svg class="meal-band" viewBox="0 0 796 140" aria-hidden="true">
    <path d="M0 22 Q398 -4 796 22 V140 Q398 96 0 140 Z" fill="var(--band-black)"/>
  </svg>

  <!-- Meal wheels -->
  <svg class="meal-wheel wheel-breakfast" viewBox="0 0 96 96" aria-label="Breakfast: 1 carb, 1 protein, 1 veggie">
    <path d="M48 48 L48 2 A46 46 0 0 1 87.8 71 Z" fill="var(--protein-blue)"/>
    <path d="M48 48 L87.8 71 A46 46 0 0 1 8.2 71 Z" fill="var(--veg-green)"/>
    <path d="M48 48 L8.2 71 A46 46 0 0 1 48 2 Z" fill="var(--carb-orange)"/>
    <circle cx="48" cy="48" r="28" fill="var(--hub-grey)" stroke="#fff" stroke-width="2"/>
    <text x="48" y="52" text-anchor="middle" font-family="Barlow Condensed, sans-serif" font-size="11" font-weight="700" fill="#fff">BREAKFAST</text>
    <g font-family="Barlow Condensed, sans-serif" font-size="11" font-weight="700" fill="#fff" text-anchor="middle">
      <text x="86" y="38">1</text><text x="48" y="92">1</text><text x="12" y="38">1</text>
    </g>
  </svg>
  <svg class="meal-wheel wheel-lunch" viewBox="0 0 96 96" aria-label="Lunch: 1 carb, 1 protein, 1 veggie">
    <path d="M48 48 L48 2 A46 46 0 0 1 87.8 71 Z" fill="var(--protein-blue)"/>
    <path d="M48 48 L87.8 71 A46 46 0 0 1 8.2 71 Z" fill="var(--veg-green)"/>
    <path d="M48 48 L8.2 71 A46 46 0 0 1 48 2 Z" fill="var(--carb-orange)"/>
    <circle cx="48" cy="48" r="28" fill="var(--hub-grey)" stroke="#fff" stroke-width="2"/>
    <text x="48" y="52" text-anchor="middle" font-family="Barlow Condensed, sans-serif" font-size="12" font-weight="700" fill="#fff">LUNCH</text>
    <g font-family="Barlow Condensed, sans-serif" font-size="11" font-weight="700" fill="#fff" text-anchor="middle">
      <text x="86" y="38">1</text><text x="48" y="92">1</text><text x="12" y="38">1</text>
    </g>
  </svg>
  <svg class="meal-wheel wheel-dinner" viewBox="0 0 96 96" aria-label="Dinner: 1 fat, 1 protein, 1 veggie">
    <path d="M48 48 L48 2 A46 46 0 0 1 87.8 71 Z" fill="var(--protein-blue)"/>
    <path d="M48 48 L87.8 71 A46 46 0 0 1 8.2 71 Z" fill="var(--veg-green)"/>
    <path d="M48 48 L8.2 71 A46 46 0 0 1 48 2 Z" fill="var(--fat-yellow)"/>
    <circle cx="48" cy="48" r="28" fill="var(--hub-grey)" stroke="#fff" stroke-width="2"/>
    <text x="48" y="52" text-anchor="middle" font-family="Barlow Condensed, sans-serif" font-size="12" font-weight="700" fill="#fff">DINNER</text>
    <g font-family="Barlow Condensed, sans-serif" font-size="11" font-weight="700" fill="#fff" text-anchor="middle">
      <text x="86" y="38">1</text><text x="48" y="92">1</text><text x="12" y="38">1</text>
    </g>
  </svg>

  <!-- Flow arrows -->
  <svg class="flow-arrow" style="left:136px;top:690px" viewBox="0 0 56 36" aria-hidden="true">
    <path d="M4 30 Q20 8 42 12" fill="none" stroke="var(--title-yellow)" stroke-width="7" stroke-linecap="round"/>
    <path d="M38 2 L54 13 L38 22 Z" fill="var(--title-yellow)"/>
  </svg>
  <svg class="flow-arrow" style="left:292px;top:690px" viewBox="0 0 56 36" aria-hidden="true">
    <path d="M4 30 Q20 8 42 12" fill="none" stroke="var(--carb-orange)" stroke-width="7" stroke-linecap="round"/>
    <path d="M38 2 L54 13 L38 22 Z" fill="var(--carb-orange)"/>
  </svg>
  <svg class="flow-arrow" style="left:446px;top:690px" viewBox="0 0 56 36" aria-hidden="true">
    <path d="M4 30 Q20 8 42 12" fill="none" stroke="var(--title-yellow)" stroke-width="7" stroke-linecap="round"/>
    <path d="M38 2 L54 13 L38 22 Z" fill="var(--title-yellow)"/>
  </svg>
  <svg class="flow-arrow" style="left:604px;top:690px" viewBox="0 0 56 36" aria-hidden="true">
    <path d="M4 30 Q20 8 42 12" fill="none" stroke="var(--carb-orange)" stroke-width="7" stroke-linecap="round"/>
    <path d="M38 2 L54 13 L38 22 Z" fill="var(--carb-orange)"/>
  </svg>

  <div class="snack snack-one">
    <span class="snack-pill">SNACK</span>
    <span class="snack-note">1/2 PORTION OF PROTEIN</span>
  </div>
  <div class="snack snack-two">
    <span class="snack-pill">SNACK</span>
    <span class="snack-note">1/2 PORTION OF PROTEIN</span>
  </div>

  <section class="tips">
    <svg class="tips-bg" viewBox="0 0 796 239" preserveAspectRatio="none" aria-hidden="true">
      <defs>
        <linearGradient id="peachGrad" x1="0" y1="0" x2="0" y2="1">
          <stop offset="0" stop-color="#f9c393"/>
          <stop offset="1" stop-color="#ffe3c6"/>
        </linearGradient>
      </defs>
      <path d="M0 22 Q398 -22 796 22 V239 H0 Z" fill="url(#peachGrad)"/>
    </svg>
    <div class="frond-deco" role="img" aria-label="Faint palm leaf pattern"></div>
    <div class="frond-deco left" role="img" aria-label="Faint palm leaf pattern"></div>

    <h2 class="tips-title"><span class="lead">FUEL YOUR</span> <span class="accent">HEATWAVE RESET!</span></h2>

    <div class="tips-body">
      <p class="tips-intro">This plan isn't about starving yourself - it's about sculpting a lean, toned physique by shredding fat while preserving muscle. Here's how to maximize your results:</p>
      <ol class="tip-list">
        <li><span class="tip-name">1. Eat Like a Champion:</span> <span class="body">Stick to this list as close as possible for maximum results, 7 Days A Week.</span></li>
        <li><span class="tip-name">2.Burn More Than You Consume:</span> <span class="body">This is the golden rule! You need to burn more calories than you consume to create a deficit and force your body to tap into fat stores for energy.</span></li>
        <li><span class="tip-name">3.Prioritize Protein:</span> <span class="body">Protein helps build and maintain muscle mass, which is crucial for boosting metabolism and burning more calories at rest.</span></li>
        <li><span class="tip-name">4.Maximize Sleep:</span> <span class="body">When sleep-deprived, your body produces more ghrelin (hunger hormone) and less leptin (satiety hormone). Aim for 7-8 hours of quality sleep nightly.</span></li>
        <li><span class="tip-name">5.Consistency is King/Queen:</span> <span class="body">Don't expect overnight results. Stick to your plan, track your progress, and celebrate small victories. Remember, slow and steady wins the reset race!</span></li>
      </ol>
    </div>
    <p class="credit">Icons by Glyphhouse from Iconbay.com</p>
  </section>

</main>
</body>
</html>
```